Quorvel Landing page redesign

We are looking for a landing page redesign before we officially launch. We want to incorporate the information already on the site at www.Quorvel-example.com landing page but make it more inviting. There needs to be a sign up section along with clearly stating what we do. Having a place for sample profiles and linking to our blog and podcast is option. More information about all we will be doing is at Quorvel is on the landing page and also on the blog.

Target Market(s)

35 years old and up.

Coding

Coded - Design and coding required

Number of Pages Required

1 page

Requirements
Must have
• The top bar and the bottom bar (with the privacy policy, etc)
• Sign in/up section.
• I don't want to give to much here because I want designers to be creative.
Nice to have
• Prefer not to have a landing page that requires a lot of scrolling at all.

```html
<!DOCTYPE html>
<html lang="en">
<head>
<meta charset="utf-8">
<title>Quorvel</title>
<link href="https://fonts.googleapis.com/css2?family=Ubuntu:wght@400;500;700&family=Open+Sans:wght@400;600;700&display=swap" rel="stylesheet">
<style>
:root{
  --navy:#1b1f5e;
  --blue-btn:#2a3aa8;
  --ink:#333;
  --grey-band:#dcdcdf;
  --white:#fff;
}
*{box-sizing:border-box;margin:0;padding:0}
html,body{width:1200px;height:937px;overflow:hidden;background:var(--white)}
body{font-family:"Open Sans",sans-serif;color:var(--ink)}
.canvas{position:relative;width:1200px;height:937px;overflow:hidden;background:linear-gradient(#fff 0,#fff 620px,#f1f1f3 700px,#d9d9dc 900px)}

/* header */
.top-bar{position:absolute;left:0;top:0;width:1200px;height:76px;border-top:3px solid var(--navy);background:linear-gradient(#fafafa,#dcdcdf)}
.header-tab{position:absolute;left:0;top:0}
.nav-link{position:absolute;top:42px;font:700 15px "Ubuntu",sans-serif;color:#3a3a3a;letter-spacing:.3px;text-decoration:none}
.brand{position:absolute;left:0;width:1200px;top:38px;text-align:center}
.brand-name{font:500 42px "Ubuntu",sans-serif;color:var(--navy);letter-spacing:.5px}

/* hero */
.hero{position:absolute;left:0;top:76px;width:1200px;height:543px;background:
 radial-gradient(ellipse 260px 160px at 380px 470px,#efe2d6 0,transparent 70%),
 radial-gradient(ellipse 220px 160px at 620px 450px,#e6dbd2 0,transparent 70%),
 radial-gradient(ellipse 300px 200px at 200px 140px,#e3e6ee 0,transparent 70%),
 radial-gradient(ellipse 300px 200px at 900px 120px,#eceaea 0,transparent 70%),
 linear-gradient(#f3f3f5,#ebeaec)}
.hero-copy{position:absolute;left:45px;top:208px;width:500px}
.hero-title{font:700 44px "Ubuntu",sans-serif;color:#333;letter-spacing:.2px;white-space:nowrap}
.hero-title span{color:var(--navy)}
.hero-lead{margin-top:20px;font:500 18.5px/24px "Ubuntu",sans-serif;color:#666}

.signup{position:absolute;left:68px;top:414px;width:461px;height:96px;background:var(--navy);border:2px solid #fff;border-radius:3px;box-shadow:0 3px 8px rgba(0,0,0,.25)}
.signup-badge{position:absolute;left:-27px;top:-25px;width:84px;height:84px;border-radius:50%;background:var(--navy);border:4px solid #fff;display:flex;align-items:center;justify-content:center}
.signup-title{position:absolute;left:100px;top:12px;font:700 17px "Ubuntu",sans-serif;color:#fff;letter-spacing:.2px}
.signup-input{position:absolute;left:72px;top:44px;width:236px;height:33px;border:1px solid #ccc;border-radius:4px;background:#fff;font:500 15px "Ubuntu",sans-serif;color:#333;padding:0 10px;line-height:33px}
.signup-btn{position:absolute;left:319px;top:44px;width:121px;height:33px;border-radius:4px;background:var(--blue-btn);color:#fff;font:700 16px "Ubuntu",sans-serif;text-align:center;line-height:33px;letter-spacing:.3px}

/* profile preview */
.preview-arrow{position:absolute;top:344px;font:700 18px "Open Sans",sans-serif;color:var(--navy)}
.preview{position:absolute;left:628px;top:161px;width:515px;height:396px;background:#fff;box-shadow:0 8px 14px rgba(0,0,0,.2);font-family:"Open Sans",sans-serif;overflow:hidden}
.pv-top{height:10px;background:var(--navy);color:#fff;font-size:5px;padding:2px 10px}
.pv-nav{position:relative;height:18px;border-bottom:1px solid #e2e2e2;font-size:5px;color:#333}
.pv-nav span{position:absolute;top:6px}
.pv-nav .pv-logo{left:238px;top:4px;font-size:7px;color:var(--navy)}
.pv-search{position:absolute;right:12px;top:4px;width:75px;height:9px;border-radius:5px;background:#ddd;color:#999;font-size:5px;padding:1px 6px}
.pv-name{position:absolute;left:0;width:515px;top:36px;text-align:center;font-size:11px;color:var(--navy)}
.pv-name b{font-weight:700}
.pv-aka{position:absolute;left:0;width:515px;top:52px;text-align:center;font-size:5px;color:#777}
.pv-label{position:absolute;font-size:7px;color:var(--navy)}
.pv-label b{font-weight:700}
.pv-photo{position:absolute;background:linear-gradient(135deg,#c9a790,#8a6c5a)}
.pv-lower{position:absolute;left:0;top:238px;width:515px;height:158px;background:#f1f2f5}
.pv-select{position:absolute;left:19px;top:12px;width:68px;height:12px;background:#fff;border:1px solid #ddd;font-size:5px;font-weight:700;padding:2px 6px}
.pv-card{position:absolute;width:80px;height:41px;background:#fff;border:1px solid #ddd;font-size:4.5px;color:#333;line-height:6px}
.pv-card .d{background:var(--navy);color:#fff;text-align:right;padding:1px 4px;font-weight:700}
.pv-card .t{font-weight:700;padding:1px 3px 0}
.pv-card .p{color:#888;padding:0 3px}
.pv-card .x{padding:3px 3px 0;color:#555}
.pv-axis{position:absolute;left:34px;top:86px;width:446px;height:1px;background:#ccc}
.pv-dot{position:absolute;top:80px;width:13px;height:13px;border-radius:50%;background:#bbb;color:#fff;font-size:8px;text-align:center;line-height:12px}

/* features */
.features{position:absolute;left:0;top:660px;width:1200px;display:flex;justify-content:space-around;padding:0 30px}
.feature{width:227px;text-align:center}
.feature-icon{width:94px;height:94px;margin:0 auto;border:3px solid var(--navy);border-radius:50%;display:flex;align-items:center;justify-content:center;background:#fff;box-shadow:0 5px 4px -3px rgba(0,0,0,.18)}
.feature-text{margin-top:16px;font:400 16.5px/19px "Open Sans",sans-serif;color:#444}
.feature-text b{color:var(--navy);font-weight:700}

/* footer */
.footer-tab{position:absolute;left:0;top:874px}
.footer-links{position:absolute;left:0;width:1200px;top:894px;text-align:center;font:600 12.5px "Open Sans",sans-serif;color:#333}
.footer-links span{margin:0 5px}
</style>
</head>
<body>
<div class="canvas">

  <section class="hero" role="img" aria-label="Softly faded photo of a family with children smiling together"></section>

  <header>
    <div class="top-bar"></div>
    <svg class="header-tab" width="1200" height="110" viewBox="0 0 1200 110" aria-hidden="true">
      <path d="M280 76 C310 76 310 104 340 104 L860 104 C890 104 890 76 920 76 Z" fill="#dcdcdf"/>
    </svg>
    <a class="nav-link" style="left:36px">BLOG</a>
    <a class="nav-link" style="left:110px">PODCAST</a>
    <a class="nav-link" style="left:1120px">LOGIN</a>
    <div class="brand"><span class="brand-name">Quorvel</span></div>
  </header>

  <div class="hero-copy">
    <h1 class="hero-title">Welcome to <span>Quorvel</span></h1>
    <p class="hero-lead">Build multiple Quorvel pages through one account for yourself, your family and to keep loved one's legacies alive.</p>
  </div>

  <form class="signup">
    <div class="signup-badge">
      <svg width="44" height="50" viewBox="0 0 44 50" aria-hidden="true" fill="none" stroke="#fff" stroke-width="2.6" stroke-linecap="round" stroke-linejoin="round">
        <path d="M11 20 A10 10 0 1 1 30 20"/>
        <path d="M6 20 A15 15 0 1 1 35 20"/>
        <path d="M16 40 L9 31 C7 28 11 25 14 28 L17 31 L17 15 C17 11 23 11 23 15 L23 25 C25 23 29 23 29 26 C31 24 35 25 35 28 C37 27 40 28 40 31 L40 40 C40 45 36 48 31 48 L22 48 C19 48 17 45 16 40 Z" fill="#fff"/>
      </svg>
    </div>
    <div class="signup-title">SIGN UP TO BECOME AN EARLY USER</div>
    <div class="signup-input">Enter Email Address</div>
    <div class="signup-btn">SUBSCRIBE</div>
  </form>

  <span class="preview-arrow" style="left:609px">&#8592;</span>
  <span class="preview-arrow" style="left:1153px">&#8594;</span>

  <div class="preview">
    <div class="pv-top">Manage Users</div>
    <div class="pv-nav">
      <span style="left:12px">+ MY PAGES</span>
      <span style="left:52px">&#9823; FAMILY &amp; FRIENDS</span>
      <span class="pv-logo">Quorvel</span>
      <span style="left:410px">&#9679;</span>
      <div class="pv-search">Search</div>
    </div>
    <div class="pv-name"><b>DANIEL</b> REED CALLOWAY</div>
    <div class="pv-aka">AKA: Dan</div>

    <div class="pv-label" style="left:14px;top:64px"><b>FAMILY</b> TREE</div>
    <svg style="position:absolute;left:14px;top:74px" width="140" height="55" viewBox="0 0 140 55" aria-hidden="true" stroke="#1b1f5e" stroke-width="1.5">
      <line x1="0" y1="1" x2="130" y2="1" stroke="#999" stroke-width=".6"/>
      <line x1="14" y1="8" x2="40" y2="8"/><line x1="112" y1="8" x2="138" y2="8"/>
      <line x1="28" y1="26" x2="52" y2="26"/><line x1="94" y1="26" x2="120" y2="26"/>
      <line x1="14" y1="44" x2="40" y2="44"/><line x1="62" y1="44" x2="88" y2="44"/><line x1="112" y1="44" x2="138" y2="44"/>
      <g fill="#ccc" stroke="none"><rect x="4" y="4" width="7" height="7"/><rect x="18" y="22" width="7" height="7"/><rect x="84" y="22" width="7" height="7"/><rect x="4" y="40" width="7" height="7"/><rect x="52" y="40" width="7" height="7"/><rect x="102" y="40" width="7" height="7"/></g>
    </svg>
    <div role="img" aria-label="World globe illustration" style="position:absolute;left:15px;top:143px;width:60px;height:60px;border-radius:50%;background:radial-gradient(circle at 40% 40%,#b7d2ea,#4a7fb5);box-shadow:0 2px 4px rgba(0,0,0,.25)"></div>
    <div class="pv-label" style="left:85px;top:166px;border-bottom:1px solid #999"><b>DEFINING</b> MAPS</div>

    <div class="pv-photo" role="img" aria-label="Profile photo of a coach in a baseball jersey" style="left:199px;top:70px;width:120px;height:120px;border-radius:50%;border:3px solid #eee;background:radial-gradient(circle at 50% 70%,#d9552a,#a63a1f 60%,#3f6b3a)"></div>
    <div class="pv-photo" role="img" aria-label="Photo of a newborn baby" style="left:373px;top:63px;width:131px;height:74px;background:linear-gradient(135deg,#9fb7d6,#e6c9b8)"></div>
    <div class="pv-photo" role="img" aria-label="Family photo" style="left:373px;top:142px;width:64px;height:70px;background:linear-gradient(135deg,#8a7a5a,#5a4a3a)"></div>
    <div class="pv-photo" role="img" aria-label="Photo of a father and young son" style="left:440px;top:142px;width:64px;height:70px;background:linear-gradient(135deg,#c56a4a,#e08a3a)"></div>
    <div style="position:absolute;left:395px;top:227px;width:109px;height:1px;background:#999"></div>
    <div class="pv-label" style="left:433px;top:229px"><b>DEFINING</b> PHOTOS</div>

    <div class="pv-lower">
      <div class="pv-select">My Life &nbsp;&nbsp;&nbsp;&nbsp;&nbsp;&nbsp;&nbsp;&nbsp;&#9662;</div>

      <div class="pv-card" style="left:97px;top:34px"><div class="d">December 8, 1976</div><div class="t">My Birth</div><div class="p">Riverton, OH</div></div>
      <div class="pv-card" style="left:178px;top:34px"><div class="d">December 15, 1999</div><div class="t">Pinecrest State Graduation</div><div class="p">Raleigh, NC</div><div class="x">Finally graduated, 5 years and...</div></div>
      <div class="pv-card" style="left:259px;top:34px"><div class="d">November 10, 2004</div><div class="t">Back to Raleigh</div><div class="p">Raleigh, NC</div><div class="x">Not all timeline events for me...</div></div>
      <div class="pv-card" style="left:340px;top:34px"><div class="d">October 19, 2014</div><div class="t">Birth of My son</div><div class="p">Chapel Hill, NC</div><div class="x">This is the best day of my life...</div></div>

      <div class="pv-axis"></div>
      <div class="pv-dot" style="left:28px">&#8249;</div>
      <div class="pv-dot" style="left:474px">&#8250;</div>

      <div class="pv-card" style="left:135px;top:96px"><div class="d">December 23, 1983</div><div class="t">House Fire</div><div class="p">Elm Grove, VA</div><div class="x">Around 5 pm at our house...</div></div>
      <div class="pv-card" style="left:216px;top:96px"><div class="d">November 15, 2001</div><div class="t">Coaching Start</div><div class="p">Baltimore, MD</div><div class="x">Took my first coaching job...</div></div>
      <div class="pv-card" style="left:297px;top:96px"><div class="d">November 1, 2009</div><div class="t">Wrestling Head Coach</div><div class="p">Wake Forest, NC</div><div class="x">Beginning in 2009, I took over...</div></div>
      <div class="pv-card" style="left:378px;top:96px"><div class="d">December 16, 2016</div><div class="t">Harbor College</div><div class="p">Charlotte, NC</div><div class="x">When this date arrives, I will...</div></div>
    </div>
  </div>

  <section class="features">
    <div class="feature">
      <div class="feature-icon">
        <svg width="58" height="58" viewBox="0 0 58 58" aria-hidden="true" fill="none" stroke="#1b1f5e" stroke-width="3" stroke-linecap="round">
          <line x1="8" y1="6" x2="8" y2="52" stroke-width="5"/>
          <line x1="8" y1="12" x2="38" y2="12"/><circle cx="28" cy="12" r="3.5" fill="#fff"/><path d="M38 8 L44 12 L38 16"/>
          <line x1="8" y1="24" x2="48" y2="24"/><circle cx="24" cy="24" r="3.5" fill="#fff"/><path d="M46 20 L52 24 L46 28"/>
          <line x1="8" y1="36" x2="40" y2="36"/><circle cx="30" cy="36" r="3.5" fill="#fff"/><path d="M40 32 L46 36 L40 40"/>
          <line x1="8" y1="47" x2="44" y2="47"/><circle cx="22" cy="47" r="3.5" fill="#fff"/><path d="M44 43 L50 47 L44 51"/>
        </svg>
      </div>
      <p class="feature-text"><b>CREATE</b> Timelines,<br>Maps, Family Trees</p>
    </div>
    <div class="feature">
      <div class="feature-icon">
        <svg width="56" height="50" viewBox="0 0 56 50" aria-hidden="true"><path d="M28 46 C8 32 3 22 3 14 C3 7 9 3 15 3 C21 3 25 6 28 11 C31 6 35 3 41 3 C47 3 53 7 53 14 C53 22 48 32 28 46 Z" fill="none" stroke="#1b1f5e" stroke-width="5" stroke-linejoin="round"/></svg>
      </div>
      <p class="feature-text"><b>MEMORIALIZE</b><br>Loved Ones</p>
    </div>
    <div class="feature">
      <div class="feature-icon">
        <svg width="62" height="46" viewBox="0 0 62 46" aria-hidden="true" fill="#1b1f5e">
          <circle cx="14" cy="10" r="7"/><path d="M2 42 L2 28 C2 21 7 19 14 19 C21 19 26 21 26 28 L26 42 Z"/>
          <circle cx="48" cy="10" r="7"/><path d="M36 42 L36 28 C36 21 41 19 48 19 C55 19 60 21 60 28 L60 42 Z"/>
          <circle cx="31" cy="20" r="6" stroke="#fff" stroke-width="2"/><path d="M21 44 L21 36 C21 30 25 28 31 28 C37 28 41 30 41 36 L41 44 Z" stroke="#fff" stroke-width="2"/>
        </svg>
      </div>
      <p class="feature-text"><b>SHARE</b> Family Stories,<br>History and more</p>
    </div>
    <div class="feature">
      <div class="feature-icon">
        <svg width="56" height="58" viewBox="0 0 56 58" aria-hidden="true">
          <path d="M24 3 L44 10 L44 26 C44 40 36 50 24 55 C12 50 4 40 4 26 L4 10 Z" fill="#1b1f5e"/>
          <circle cx="40" cy="42" r="12" fill="#fff" stroke="#1b1f5e" stroke-width="3"/>
          <path d="M34 42 L39 47 L47 37" fill="none" stroke="#1b1f5e" stroke-width="3.5" stroke-linecap="round" stroke-linejoin="round"/>
        </svg>
      </div>
      <p class="feature-text"><b>CONTROL</b><br>Your Privacy</p>
    </div>
    <div class="feature">
      <div class="feature-icon">
        <svg width="62" height="62" viewBox="0 0 62 62" aria-hidden="true">
          <circle cx="31" cy="31" r="26" fill="none" stroke="#1b1f5e" stroke-width="4"/>
          <path d="M16 26 L24 26 L38 17 L38 45 L24 36 L16 36 Z" fill="#1b1f5e"/>
          <path d="M43 24 C46 28 46 34 43 38 M47 20 C52 26 52 36 47 42" fill="none" stroke="#1b1f5e" stroke-width="2.5" stroke-linecap="round"/>
          <line x1="13" y1="49" x2="49" y2="13" stroke="#1b1f5e" stroke-width="4"/>
        </svg>
      </div>
      <p class="feature-text"><b>NO</b> Ads,<br><b>NO</b> Like Buttons<br><b>NO</b> News Feeds</p>
    </div>
  </section>

  <footer>
    <svg class="footer-tab" width="1200" height="63" viewBox="0 0 1200 63" aria-hidden="true">
      <path d="M300 63 C325 63 330 0 360 0 L860 0 C890 0 895 63 920 63 Z" fill="#fff"/>
    </svg>
    <div class="footer-links">
      <span>Privacy Policy</span>I<span>Terms of Use</span>I<span>Data Tracking Policy</span>I<span>Submit Feedback</span>I<span>Quorvel &copy; 2017</span>
    </div>
  </footer>

</div>
</body>
</html>
```